Heating, ventilation and air conditioning (Hvac) company needs a van wrap design

We need a van wrap design for Norvale Climate Works Inc., a company performing work in Greater Toronto Area, Ontario, Canada.
Most of our work is installing complete HVAC Systems in custom build homes, renovations and small commercial applications. We specialize in custom sheet metal installation. We also install and do maintenance on furnaces, air conditionings, fireplaces, water tank heaters, etc.
We would like our design to have the 2 colours from our company logo.
We would like simple and modern design covering both sides plus back of the van. We would like the sides to be covered only half way starting from the back and ending half way on a sliding door.
The design will go on 2017 Valtera Roamer WB 170 and 2016 Valtera Roamer WB 144

Font styles to use
Sans Serif

Colors
3176b5
ec1f27

Requirements
Must have
• Phone number: 905-555-0148
Website: www.norvaleclimate.example
Email: info@norvaleclimate.example
Follow Us with Snapfold and Friendlane Icons
Also: PBRC # 000381642 on the back of the van bottom right corner

```html
<!DOCTYPE html>
<html lang="en">
<head>
<meta charset="utf-8">
<title>Norvale Climate Works – Van Wrap</title>
<link href="https://fonts.googleapis.com/css2?family=Russo+One&family=Roboto:wght@400;500;700&family=Roboto+Slab:wght@300&display=swap" rel="stylesheet">
<style>
  :root {
    --blue: #3a70b8;
    --red: #e8575a;
    --white: #ffffff;
    --stage: #ececec;
    --edge: #d6d6d6;
  }
  * { margin: 0; padding: 0; box-sizing: border-box; }
  html, body { width: 830px; height: 1200px; overflow: hidden; }
  body { background: var(--stage); font-family: "Roboto", sans-serif; position: relative; }

  .wrap-panel {
    position: absolute;
    background: var(--white);
    border: 1px solid var(--edge);
    border-radius: 14px;
    overflow: hidden;
  }
  .wrap-panel svg.artwork { position: absolute; inset: 0; width: 100%; height: 100%; }
  .side-driver { left: 35px; top: 20px; width: 760px; height: 330px; }
  .side-passenger { left: 35px; top: 370px; width: 760px; height: 330px; }
  .rear-doors { left: 215px; top: 720px; width: 400px; height: 460px; }

  .brand-block { position: absolute; top: 26px; text-align: center; }
  .brand-name {
    font-family: "Russo One", sans-serif;
    color: var(--blue);
    font-size: 24px;
    font-weight: 400;
    letter-spacing: 0.5px;
    white-space: nowrap;
  }
  .tagline {
    margin-top: 6px;
    font-family: "Roboto Slab", serif;
    font-weight: 300;
    color: var(--blue);
    font-size: 13px;
    letter-spacing: 0.5px;
    white-space: nowrap;
  }
  .phone {
    position: absolute;
    font-family: "Roboto", sans-serif;
    font-weight: 700;
    color: var(--blue);
    font-size: 36px;
    letter-spacing: 1px;
    white-space: nowrap;
  }
  .contact {
    position: absolute;
    color: var(--white);
    font-size: 13px;
    font-weight: 500;
    line-height: 20px;
    text-transform: uppercase;
    white-space: nowrap;
  }
  .follow {
    position: absolute;
    color: var(--white);
    font-size: 20px;
    display: flex;
    align-items: center;
    gap: 10px;
    white-space: nowrap;
  }
  .social {
    display: flex;
    align-items: center;
    gap: 4px;
    font-size: 13px;
    font-weight: 500;
  }
  .social-square { width: 12px; height: 12px; background: var(--white); border-radius: 2px; }
  .license {
    position: absolute;
    color: var(--white);
    font-size: 13px;
    font-weight: 500;
    white-space: nowrap;
  }

  /* driver side positions */
  .side-driver .brand-block { right: 18px; }
  .side-driver .phone { left: 44px; top: 182px; }
  .side-driver .contact { right: 18px; top: 238px; text-align: right; }
  .side-driver .follow { left: 380px; top: 290px; }

  /* passenger side positions */
  .side-passenger .brand-block { left: 18px; }
  .side-passenger .phone { right: 44px; top: 182px; }
  .side-passenger .contact { left: 18px; top: 238px; }
  .side-passenger .follow { left: 80px; top: 290px; }

  /* rear positions */
  .rear-doors .brand-block { left: 0; right: 0; top: 148px; }
  .rear-doors .brand-name { font-size: 22px; }
  .rear-doors .tagline { font-size: 11px; }
  .rear-doors .phone { left: 0; right: 0; text-align: center; top: 340px; color: var(--white); font-size: 32px; }
  .rear-doors .license { right: 28px; top: 418px; }
</style>
</head>
<body>

<!-- Driver side -->
<section class="wrap-panel side-driver">
  <svg class="artwork" viewBox="0 0 760 330" aria-hidden="true">
    <path d="M250 330 C380 240 560 205 760 190 L760 330 Z" fill="var(--blue)"/>
    <path d="M200 330 C340 225 540 180 760 160 L760 176 C550 192 370 232 230 330 Z" fill="var(--blue)"/>
    <path d="M150 330 C310 210 520 160 740 140 C530 168 340 222 185 330 Z" fill="var(--red)"/>
    <circle cx="325" cy="108" r="64" fill="none" stroke="var(--red)" stroke-width="10"/>
    <text x="325" y="115" text-anchor="middle" font-family="Russo One, sans-serif" font-size="19" fill="var(--blue)">NORVALE</text>
  </svg>
  <div class="brand-block">
    <h1 class="brand-name">NORVALE CLIMATE WORKS</h1>
    <p class="tagline">YOUR TRUSTED HVAC EXPERTS</p>
  </div>
  <p class="phone">905-555-0148</p>
  <p class="contact">www.norvaleclimate.example<br>info@norvaleclimate.example</p>
  <div class="follow">FOLLOW US
    <span class="social"><span class="social-square"></span>Friendlane</span>
    <span class="social"><span class="social-square"></span>Snapfold</span>
  </div>
</section>

<!-- Passenger side -->
<section class="wrap-panel side-passenger">
  <svg class="artwork" viewBox="0 0 760 330" aria-hidden="true">
    <g transform="translate(760 0) scale(-1 1)">
      <path d="M250 330 C380 240 560 205 760 190 L760 330 Z" fill="var(--blue)"/>
      <path d="M200 330 C340 225 540 180 760 160 L760 176 C550 192 370 232 230 330 Z" fill="var(--blue)"/>
      <path d="M150 330 C310 210 520 160 740 140 C530 168 340 222 185 330 Z" fill="var(--red)"/>
    </g>
    <circle cx="435" cy="108" r="64" fill="none" stroke="var(--red)" stroke-width="10"/>
    <text x="435" y="115" text-anchor="middle" font-family="Russo One, sans-serif" font-size="19" fill="var(--blue)">NORVALE</text>
  </svg>
  <div class="brand-block">
    <h2 class="brand-name">NORVALE CLIMATE WORKS</h2>
    <p class="tagline">YOUR TRUSTED HVAC EXPERTS</p>
  </div>
  <p class="phone">905-555-0148</p>
  <p class="contact">www.norvaleclimate.example<br>info@norvaleclimate.example</p>
  <div class="follow">FOLLOW US
    <span class="social"><span class="social-square"></span>Friendlane</span>
    <span class="social"><span class="social-square"></span>Snapfold</span>
  </div>
</section>

<!-- Rear doors -->
<section class="wrap-panel rear-doors">
  <svg class="artwork" viewBox="0 0 400 460" aria-hidden="true">
    <path d="M0 460 L0 330 C120 290 260 262 400 245 L400 460 Z" fill="var(--blue)"/>
    <path d="M0 300 C130 260 270 232 400 218 L400 232 C270 246 130 275 0 316 Z" fill="var(--blue)"/>
    <path d="M0 285 C130 245 270 215 390 202 C270 225 130 258 0 300 Z" fill="var(--red)"/>
    <circle cx="200" cy="80" r="50" fill="none" stroke="var(--red)" stroke-width="8"/>
    <text x="200" y="86" text-anchor="middle" font-family="Russo One, sans-serif" font-size="15" fill="var(--blue)">NORVALE</text>
  </svg>
  <div class="brand-block">
    <h2 class="brand-name">NORVALE CLIMATE WORKS</h2>
    <p class="tagline">YOUR TRUSTED HVAC EXPERTS</p>
  </div>
  <p class="phone">905-555-0148</p>
  <p class="license">PBRC # 000381642</p>
</section>

</body>
</html>
```